Design eines Praxisschilds für Hausarztpraxis
Zielgruppe
Hausarztpraxis, Zielgruppe sind die Bewohner vor Ort, bodenständig
Aufgabenstellung
Praxisschild entwerfen, es soll schlicht sein. Das angefügte Logo bitte verwenden, ggf. auch nur das Symbol ohne Namen verwenden und den Namen extra in schwarz aufführen.
Farben:
- schwarz
- Pantone 13-0645 Limeade
- Pantone 7726
Text:
Dr. med. Jonas Walbrecht
Facharzt für Innere Medizin
Facharzt für Allgemeinmedizin
Sprechzeiten:
Montag bis Freitag 07:30 – 12:00 Uhr
Dienstag und Donnerstag 17:00 – 19:00 Uhr
und nach Vereinbarung
Tel: 0761 83172
www.hausarzt-beispielau.de
Format quer (die Maße sind leider vorgegeben): 55,7 cm x 42,8 cm

```html
<!DOCTYPE html>
<html lang="de">
<head>
<meta charset="utf-8">
<title>Praxisschild – Dr. Jonas Walbrecht</title>
<link rel="stylesheet" href="https://fonts.googleapis.com/css2?family=Hanken+Grotesk:wght@600;700&family=Lexend:wght@400;600&display=swap">
<style>
  :root {
    --praxis-green: #2a7a52;
    --limeade: #d3d962;
    --paper: #ffffff;
    --muted: #b5b5b5;
  }
  html, body {
    margin: 0;
    padding: 0;
    width: 1200px;
    height: 922px;
    overflow: hidden;
    background: var(--praxis-green);
  }
  .sign {
    position: relative;
    width: 1200px;
    height: 922px;
    background: var(--praxis-green);
  }
  .sign__panel {
    position: absolute;
    left: 39px;
    top: 73px;
    width: 1120px;
    height: 775px;
    background: var(--paper);
  }
  .brand-mark {
    position: absolute;
    left: 91px;
    top: 93px;
    width: 188px;
    height: 188px;
    border-radius: 50%;
    background: var(--limeade);
  }
  .brand-divider {
    position: absolute;
    left: 343px;
    top: 92px;
    width: 2px;
    height: 189px;
    background: var(--praxis-green);
  }
  .brand-name,
  .brand-tagline {
    position: absolute;
    left: 384px;
    width: 720px;
    margin: 0;
    font-family: "Lexend", sans-serif;
    font-weight: 600;
    color: var(--praxis-green);
    white-space: nowrap;
  }
  .brand-name {
    top: 118px;
    font-size: 74px;
    line-height: 1;
    letter-spacing: -0.01em;
  }
  .brand-tagline {
    top: 208px;
    font-size: 32px;
    line-height: 1;
    letter-spacing: 0.27em;
  }
  .hours {
    position: absolute;
    left: 0;
    width: 1200px;
    text-align: center;
    font-family: "Hanken Grotesk", sans-serif;
    font-weight: 700;
    color: var(--praxis-green);
    margin: 0;
    line-height: 1;
  }
  .hours__title {
    top: 328px;
    font-size: 31px;
    letter-spacing: 0.42em;
    color: var(--limeade);
    padding-left: 0.42em;
  }
  .hours__title .colon { color: var(--muted); }
  .hours__line { font-size: 46px; }
  .hours__line--weekdays { top: 398px; }
  .hours__line--evenings { top: 517px; }
  .hours__line--appointment { top: 637px; }
  .contact { font-size: 31px; font-weight: 600; }
  .contact--phone { top: 749px; }
  .contact--web { top: 794px; }
</style>
</head>
<body>
  <main class="sign">
    <div class="sign__panel"></div>

    <div class="brand-mark" aria-hidden="true"></div>
    <div class="brand-divider" aria-hidden="true"></div>
    <h1 class="brand-name">Dr. Jonas Walbrecht</h1>
    <p class="brand-tagline">IHR HAUSARZT IN BEISPIELAU</p>

    <h2 class="hours hours__title">SPRECHZEITEN<span class="colon">:</span></h2>
    <p class="hours hours__line hours__line--weekdays">Montag bis Freitag 07:30 – 12:00 Uhr</p>
    <p class="hours hours__line hours__line--evenings">Dienstag und Donnerstag 17:00 – 19:00 Uhr</p>
    <p class="hours hours__line hours__line--appointment">und nach Vereinbarung</p>

    <p class="hours contact contact--phone">Tel: 0761 83172</p>
    <p class="hours contact contact--web">www.hausarzt-beispielau.de</p>
  </main>
</body>
</html>
```